Metal Recycling Website Require New Design for upgrade

Our company currently have an existing website, www.tavorinmetal.com and the website is generally outdated so we would like an improvement.

We would generally prefer to keep the current color theme of our website as it is similar to our current logo.

We would also like our company factory picture to be on somewhere of the webpage (but only if the designer think that the picture can blend well with the color theme)

Our company is dealing alot Aluminiun, Stainless Steel, Copper, Brass, Iron

Pictures uploaded.

Target Market(s)

General Commercial Manufacturer, B2B

Industry/Entity Type

Recycling

Number of Pages Required

1 page

Colors

Designer to choose colors to be used in the design.

Requirements
Must have
• Hopefully color will be similar to my logo theme but designer welcome to have their own input.
Nice to have
• Company Picture (Uploaded in the file)

```html
<!DOCTYPE html>
<html lang="en">
<head>
<meta charset="utf-8">
<title>Tavorin Metal Recycling</title>
<link href="https://fonts.googleapis.com/css2?family=Montserrat:wght@400;500;600;700;800;900&display=swap" rel="stylesheet">
<style>
:root{
  --gold:#d9a21a;
  --gold-dark:#b97c06;
  --gold-light:#f0b92a;
  --ink:#1e1e1e;
  --grey:#8a8a8a;
  --dark:#1b1b1b;
  --diamond:#3b3b3b;
  --cream:#f8eed3;
  --white:#ffffff;
  --sky:#6f9fd2;
}
*{box-sizing:border-box;margin:0;padding:0}
html,body{width:1200px;height:3189px;overflow:hidden}
body{position:relative;font-family:"Montserrat",sans-serif;color:var(--ink);background:var(--white)}
.abs{position:absolute}
a{color:inherit;text-decoration:none}

/* header */
.topbar{left:0;top:0;width:1200px;height:101px;background:var(--white)}
.call{right:144px;top:22px;display:flex;align-items:center;gap:10px;font-weight:700;font-size:21px}
.call .ring{width:38px;height:38px;border:2px solid var(--gold);border-radius:50%;display:flex;align-items:center;justify-content:center}
.navbar{left:0;top:81px;width:1200px;height:40px;background:linear-gradient(180deg,var(--gold-light),var(--gold-dark))}
.nav{top:81px;height:40px;display:flex;font-size:13px;font-weight:600;color:var(--white)}
.nav a{padding:0 19px;line-height:40px}
.nav a.active{background:#555}
.nav-left{left:144px}
.nav-right{left:774px}
.brand-tab{left:476px;top:81px;width:248px;height:46px;background:var(--white);clip-path:polygon(0 0,100% 0,92% 100%,8% 100%)}
.brand{left:476px;top:15px;width:248px;text-align:center}
.brand .mark{display:inline-block;width:52px;height:52px;border:3px solid var(--gold)}
.brand .name{font-size:17px;font-weight:700;color:var(--gold);letter-spacing:1px;margin-top:10px;line-height:1}

/* hero */
.hero{left:0;top:121px;width:1200px;height:620px;background:linear-gradient(180deg,#5e8fca 0%,#a8c4e0 45%,#6b6d74 65%,#3e3e42 100%)}
.hero-cut{left:0;top:590px}
.title-box{left:353px;top:204px;width:498px;height:224px;border:3px solid var(--gold);background:rgba(70,86,110,.85);text-align:center;padding-top:44px;font-weight:900;line-height:1}
.title-box .l1{color:var(--gold);font-size:60px}
.title-box .l2{color:var(--white);font-size:62px;margin-top:6px}
.slide-arrow{width:34px;height:34px;border-radius:50%;background:rgba(60,60,60,.7);border:1px solid rgba(255,255,255,.6)}
.slide-arrow svg{display:block;margin:9px auto}

/* diamonds */
.diamond{width:356px;height:356px}
.diamond .shape{position:absolute;left:52px;top:52px;width:252px;height:252px;border-radius:24px;transform:rotate(45deg);background:var(--diamond)}
.diamond.gold .shape{background:linear-gradient(135deg,var(--gold-light),var(--gold-dark))}
.diamond .body{position:absolute;left:0;top:56px;width:356px;text-align:center;color:var(--white)}
.diamond h3{font-size:17px;font-weight:700;margin-top:14px}
.diamond p{font-size:12px;line-height:18px;margin-top:12px}
.pill{display:inline-block;margin-top:18px;background:var(--white);color:#333;font-size:11px;font-weight:700;padding:8px 16px;border-radius:16px}
.diamond.gold .pill{color:var(--gold)}

/* about */
.about-photo{left:188px;top:1007px;width:351px;height:342px;background:linear-gradient(135deg,#7a6a44,#d7cfa8 50%,#6b5b36)}
.about-photo .inner{position:absolute;left:18px;top:18px;right:18px;bottom:18px;background:var(--white)}
.about-photo .badge{position:absolute;left:50%;top:50%;width:180px;height:180px;margin:-90px 0 0 -90px;border-radius:50%;background:linear-gradient(135deg,#8c7a4f,#e5dcb8,#7c6a40)}
.about-text{left:612px;top:1015px;width:390px}
.h2{font-size:42px;font-weight:800;color:var(--ink)}
.about-text p{font-size:12px;line-height:24.8px;color:var(--grey);margin-top:22px}
.outline-btn{display:inline-block;margin-top:28px;border:2px solid var(--gold);color:var(--gold);border-radius:24px;padding:13px 22px;font-weight:700;font-size:15px}

/* news */
.news{left:0;top:1458px;width:1200px;height:641px;background:var(--cream)}
.center{text-align:center;width:1200px;left:0}
.card{width:287px;top:1650px}
.card .photo{height:188px}
.card .box{margin:-26px 11px 0;background:var(--white);box-shadow:0 3px 8px rgba(0,0,0,.08);text-align:center;padding:24px 18px 22px;position:relative}
.card h4{font-size:16px;font-weight:600}
.card p{font-size:11px;line-height:21px;color:var(--grey);margin-top:12px}
.card .more{display:inline-block;margin-top:14px;color:var(--gold);font-weight:700;font-size:12px}

/* contact */
.touch-icon{width:88px;height:88px;border-radius:50%;border:2px solid var(--gold);display:flex;align-items:center;justify-content:center}
.touch-icon.filled{background:linear-gradient(180deg,var(--gold-light),var(--gold-dark));border:none}
.touch-label{width:240px;text-align:center;font-size:14px;line-height:23px;color:var(--grey)}
.field{height:46px;border:1px solid #cfcfcf;font-size:13px;color:#555;padding:0 20px;line-height:44px;background:var(--white)}
.submit{left:490px;top:2744px;width:220px;height:55px;border-radius:28px;background:linear-gradient(180deg,var(--gold-light),var(--gold-dark));color:var(--white);font-weight:700;font-size:15px;display:flex;align-items:center;justify-content:center;gap:8px}
.skyline{left:0;top:2810px;width:1200px;height:190px;background:linear-gradient(180deg,rgba(255,255,255,0),rgba(225,225,225,.5))}

/* footer */
.footer-wave{left:0;top:2870px}
.social{top:2950px;width:40px;height:40px;border:2px solid var(--white);border-radius:50%}
.foot-item{top:3025px;display:flex;align-items:center;gap:12px;color:var(--white);font-size:13px;line-height:18px}
.foot-ring{width:38px;height:38px;border-radius:50%;border:2px solid var(--white);display:flex;align-items:center;justify-content:center;flex:none}
.foot-ring.gold{background:var(--gold);border-color:var(--gold)}
.foot-nav{top:3089px;color:var(--white);font-size:15px;font-weight:600;word-spacing:2px}
.copy{top:3131px;color:var(--white);font-size:11px}
</style>
</head>
<body>

<!-- header -->
<div class="abs topbar"></div>
<div class="abs navbar"></div>
<nav class="abs nav nav-left"><a class="active">HOME</a><a>ABOUT US</a><a>PRODUCTS</a></nav>
<nav class="abs nav nav-right"><a>OUR SERVICES</a><a>CONTACT US</a></nav>
<div class="abs brand-tab"></div>
<div class="abs brand"><span class="mark"></span><div class="name">TAVORIN METAL</div></div>
<div class="abs call">
  <span class="ring"><svg width="18" height="18" viewBox="0 0 24 24"><path fill="#d9a21a" d="M6.6 10.8a15 15 0 006.6 6.6l2.2-2.2c.3-.3.7-.4 1-.2 1.1.4 2.3.6 3.6.6.6 0 1 .4 1 1V20c0 .6-.4 1-1 1A17 17 0 013 4c0-.6.4-1 1-1h3.5c.6 0 1 .4 1 1 0 1.3.2 2.5.6 3.6.1.3 0 .7-.2 1z"/></svg></span>
  Call us : +65-9000 1234
</div>

<!-- hero -->
<div class="abs hero" role="img" aria-label="Pile of shredded scrap metal under a blue sky"></div>
<svg class="abs hero-cut" width="1200" height="160" viewBox="0 0 1200 160"><path d="M0 0 Q600 230 1200 0 L1200 160 L0 160 Z" fill="#fff"/></svg>
<div class="abs title-box"><div class="l1">TAVORIN METAL</div><div class="l2">RECYCLING</div></div>
<div class="abs slide-arrow" style="left:82px;top:299px"><svg width="14" height="14" viewBox="0 0 14 14"><path d="M9 2L4 7l5 5" stroke="#fff" stroke-width="2" fill="none"/></svg></div>
<div class="abs slide-arrow" style="left:1083px;top:299px"><svg width="14" height="14" viewBox="0 0 14 14"><path d="M5 2l5 5-5 5" stroke="#fff" stroke-width="2" fill="none"/></svg></div>

<div class="abs diamond" style="left:144px;top:528px">
  <div class="shape"></div>
  <div class="body">
    <svg width="70" height="70" viewBox="0 0 70 70" fill="none" stroke="#fff" stroke-width="2"><circle cx="35" cy="16" r="8"/><path d="M10 58l8-14 8 14z"/><rect x="46" y="44" width="14" height="14"/><path d="M28 34a8 8 0 0114 0M42 40a8 8 0 01-14 0"/></svg>
    <h3>FOR INDIVIDUAL</h3>
    <p>Do Your Part, Recycle<br>With Us Today</p>
    <span class="pill">READ MORE ➜</span>
  </div>
</div>
<div class="abs diamond gold" style="left:422px;top:528px">
  <div class="shape"></div>
  <div class="body">
    <svg width="70" height="70" viewBox="0 0 70 70" fill="none" stroke="#fff" stroke-width="2"><path d="M12 30h46v30H12zM8 22h54l-4 8H12z"/><circle cx="42" cy="46" r="8"/><path d="M22 6v14M17 15l5 5 5-5M35 6v14M30 15l5 5 5-5M48 6v14M43 15l5 5 5-5"/></svg>
    <h3>FOR CORPORATE</h3>
    <p>Get The Best Value For<br>Your Scrap</p>
    <span class="pill">READ MORE ➜</span>
  </div>
</div>
<div class="abs diamond" style="left:699px;top:528px">
  <div class="shape"></div>
  <div class="body">
    <svg width="70" height="70" viewBox="0 0 70 70" fill="none" stroke="#fff" stroke-width="2"><circle cx="35" cy="35" r="13"/><path d="M22 35h26M35 22v26M8 8l17 17M62 8L45 25M8 62l17-17M62 62L45 45M35 2v12M35 56v12M2 35h12M56 35h12"/><circle cx="8" cy="8" r="3"/><circle cx="62" cy="8" r="3"/><circle cx="8" cy="62" r="3"/><circle cx="62" cy="62" r="3"/></svg>
    <h3>FOR INTERNATIONAL</h3>
    <p>Your Trusted Global<br>Partner</p>
    <span class="pill">READ MORE ➜</span>
  </div>
</div>

<!-- about -->
<div class="abs about-photo" role="img" aria-label="Polished stainless steel pieces framing a white panel">
  <div class="inner"><div class="badge"></div></div>
</div>
<div class="abs about-text">
  <h2 class="h2">ABOUT US</h2>
  <p>Tavorin Metal Recycling primary activities are the procurement, processing, recycling and trading of all ferrous and non-ferrous scrap metals, industrial scraps and other recyclables.<br>We provide full-service ferrous and non-ferrous metal recycler and processor. Recognized as an industry leader in metal recycling, our team of experienced staff and trader understand the intricacies of scrap metal recycling.</p>
  <a class="outline-btn">READ MORE ➜</a>
</div>

<!-- news -->
<div class="abs news"></div>
<h2 class="abs h2 center" style="top:1552px">LATEST NEWS</h2>
<svg class="abs" style="left:62px;top:1745px" width="36" height="66" viewBox="0 0 36 66"><path d="M34 2L3 33l31 31" stroke="#aaa" stroke-width="1.5" fill="none"/></svg>
<svg class="abs" style="left:1102px;top:1745px" width="36" height="66" viewBox="0 0 36 66"><path d="M2 2l31 31L2 64" stroke="#aaa" stroke-width="1.5" fill="none"/></svg>

<div class="abs card" style="left:145px">
  <div class="photo" role="img" aria-label="Stacked rusty metal pipes and beams" style="background:linear-gradient(135deg,#6b4a36,#b9a08a,#5e5450)"></div>
  <div class="box"><h4>Lorem ipsum dolor sit</h4><p>Sed ut perspiciatis unde omnis iste natus error sit voluptatem accusantium doloremque laudantium</p><a class="more">READ MORE ➜</a></div>
</div>
<div class="abs card" style="left:456px">
  <div class="photo" role="img" aria-label="Excavator working in a scrap yard at sunset" style="background:linear-gradient(180deg,#8db5de,#e0a35a 60%,#6a4b34)"></div>
  <div class="box"><h4>Lorem ipsum dolor sit</h4><p>Sed ut perspiciatis unde omnis iste natus error sit voluptatem accusantium doloremque laudantium</p><a class="more">READ MORE ➜</a></div>
</div>
<div class="abs card" style="left:767px">
  <div class="photo" role="img" aria-label="Pile of shiny stainless steel tubes" style="background:linear-gradient(135deg,#3c3c3c,#cfcfcf,#555)"></div>
  <div class="box"><h4>Lorem ipsum dolor sit</h4><p>Sed ut perspiciatis unde omnis iste natus error sit voluptatem accusantium doloremque laudantium</p><a class="more">READ MORE ➜</a></div>
</div>

<!-- contact -->
<h2 class="abs h2 center" style="top:2196px">GET IN TOUCH</h2>
<div class="abs touch-icon" style="left:304px;top:2295px"><svg width="30" height="30" viewBox="0 0 24 24"><path fill="#d9a21a" d="M6.6 10.8a15 15 0 006.6 6.6l2.2-2.2c.3-.3.7-.4 1-.2 1.1.4 2.3.6 3.6.6.6 0 1 .4 1 1V20c0 .6-.4 1-1 1A17 17 0 013 4c0-.6.4-1 1-1h3.5c.6 0 1 .4 1 1 0 1.3.2 2.5.6 3.6.1.3 0 .7-.2 1z"/></svg></div>
<div class="abs touch-icon filled" style="left:527px;top:2295px"><svg width="26" height="32" viewBox="0 0 24 30"><path fill="#fff" d="M12 0a10 10 0 00-10 10c0 7.5 10 20 10 20s10-12.5 10-20A10 10 0 0012 0zm0 14a4 4 0 110-8 4 4 0 010 8z"/></svg></div>
<div class="abs touch-icon" style="left:776px;top:2295px"><svg width="34" height="26" viewBox="0 0 34 26"><rect width="34" height="26" rx="2" fill="#d9a21a"/><path d="M2 3l15 11L32 3" stroke="#fff" stroke-width="2" fill="none"/></svg></div>
<div class="abs touch-label" style="left:228px;top:2398px">Phone<br>+65-9000 1234</div>
<div class="abs touch-label" style="left:451px;top:2398px">18, Kelvar Industrial Rd,<br>Singapore 730118</div>
<div class="abs touch-label" style="left:700px;top:2398px">Email<br>sales@tavorinmetal.com</div>

<div class="abs field" style="left:145px;top:2512px;width:213px">Name</div>
<div class="abs field" style="left:378px;top:2512px;width:213px">Email</div>
<div class="abs field" style="left:611px;top:2512px;width:212px">Phone</div>
<div class="abs field" style="left:843px;top:2512px;width:212px">Address<svg style="position:absolute;right:14px;top:19px" width="10" height="6" viewBox="0 0 10 6"><path d="M0 0h10L5 6z" fill="#444"/></svg></div>
<div class="abs field" style="left:145px;top:2580px;width:910px;height:131px">Message</div>
<div class="abs skyline" role="img" aria-label="Faint line drawing of a city skyline"></div>
<a class="abs submit">SUBMIT MESSAGE ➜</a>

<!-- footer -->
<svg class="abs footer-wave" width="1200" height="319" viewBox="0 0 1200 319">
  <path d="M0 165 Q600 -60 1200 165 L1200 319 L0 319 Z" fill="#e0a61e"/>
  <path d="M0 180 Q600 -40 1200 180 L1200 319 L0 319 Z" fill="#1b1b1b"/>
</svg>
<div class="abs social" style="left:500px"></div>
<div class="abs social" style="left:553px"></div>
<div class="abs social" style="left:606px"></div>
<div class="abs social" style="left:659px"></div>

<div class="abs foot-item" style="left:241px">
  <span class="foot-ring"><svg width="14" height="18" viewBox="0 0 24 30"><path fill="#d9a21a" d="M12 0a10 10 0 00-10 10c0 7.5 10 20 10 20s10-12.5 10-20A10 10 0 0012 0zm0 14a4 4 0 110-8 4 4 0 010 8z"/></svg></span>
  <span>18, Kelvar Industrial Rd,<br>Singapore 730118</span>
</div>
<div class="abs foot-item" style="left:488px">
  <span class="foot-ring"><svg width="16" height="16" viewBox="0 0 24 24"><path fill="#d9a21a" d="M6.6 10.8a15 15 0 006.6 6.6l2.2-2.2c.3-.3.7-.4 1-.2 1.1.4 2.3.6 3.6.6.6 0 1 .4 1 1V20c0 .6-.4 1-1 1A17 17 0 013 4c0-.6.4-1 1-1h3.5c.6 0 1 .4 1 1 0 1.3.2 2.5.6 3.6.1.3 0 .7-.2 1z"/></svg></span>
  <span>Call : +65-9000 1234</span>
</div>
<div class="abs foot-item" style="left:711px">
  <span class="foot-ring gold"><svg width="18" height="14" viewBox="0 0 34 26"><rect width="34" height="26" rx="2" fill="#fff"/><path d="M2 3l15 11L32 3" stroke="#d9a21a" stroke-width="3" fill="none"/></svg></span>
  <span>Email : sales@tavorinmetal.com</span>
</div>

<div class="abs foot-nav center">HOME &nbsp; / &nbsp; ABOUT US &nbsp; / &nbsp; PRODUCTS &nbsp; / &nbsp; OUR SERVICES &nbsp; / &nbsp; CONTACT US</div>
<div class="abs copy center">Copyrights @ 2019 All Rights Reserved &nbsp;|&nbsp; Privacy Policy</div>

</body>
</html>
```